Gin Bottle Label - 'Lantern Down Lane'

I would like a label designing for our gin. The name is based on a saying 'Lantern down lane' meaning stopping for one last drink before leaving. Id like the label to either show humour or people walking? The wording should be the focus.
Attaches are the company logo and a few ideas for you.

```html
<!DOCTYPE html>
<html lang="en">
<head>
<meta charset="utf-8">
<title>Lantern Down Lane Gin Label</title>
<link href="https://fonts.googleapis.com/css2?family=Abril+Fatface&family=Playfair+Display:wght@700;900&family=Pinyon+Script&display=swap" rel="stylesheet">
<style>
  :root {
    --backdrop: #dfe3e8;
    --parchment: #efe6cf;
    --parchment-edge: #d9ccac;
    --frame: #6b5a3e;
    --title-red: #b3261e;
    --title-shadow: #3a1a12;
    --ink: #3b3024;
    --ribbon: #c9a85a;
    --ribbon-dark: #8f7232;
    --scene-sky: #e9dcd0;
    --scene-road: #b9a29a;
    --figure: #6a4a32;
  }
  * { box-sizing: border-box; margin: 0; padding: 0; }
  html, body {
    width: 798px; height: 1200px; overflow: hidden;
    background: var(--backdrop);
  }
  .canvas { position: relative; width: 798px; height: 1200px; }
  .label {
    position: absolute; left: 69px; top: 260px;
    width: 660px; height: 680px;
    background: var(--parchment);
    border: 2px solid var(--parchment-edge);
  }
  .label__frame {
    position: absolute; inset: 16px;
    border: 3px solid var(--frame);
    outline: 1px solid var(--frame);
    outline-offset: 6px;
  }
  .maker {
    position: absolute; top: 40px; left: 0; right: 0;
    display: flex; align-items: center; justify-content: center; gap: 10px;
    font-family: 'Playfair Display', serif; font-weight: 700;
    font-size: 15px; letter-spacing: 2px; text-transform: uppercase;
    color: var(--ink);
  }
  .maker__dot {
    width: 18px; height: 18px; border-radius: 50%;
    border: 2px solid var(--ink);
  }
  .product-name {
    position: absolute; left: 80px; top: 92px; z-index: 3;
    font-family: 'Abril Fatface', serif; font-weight: 400;
    font-size: 72px; line-height: 0.95;
    color: var(--title-red);
    text-shadow: 2px 2px 0 var(--title-shadow);
    text-transform: uppercase;
  }
  .scene {
    position: absolute; left: 200px; top: 262px; z-index: 1;
    width: 400px; height: 130px;
    background: linear-gradient(180deg, var(--scene-sky) 0%, var(--scene-road) 100%);
  }
  .traveller {
    position: absolute; left: 120px; top: 250px; z-index: 2;
    width: 110px; height: 310px;
    background: linear-gradient(180deg, #3a2a1e 0%, var(--figure) 40%, #4a3322 100%);
    border-radius: 40px 40px 10px 10px;
  }
  .spirit {
    position: absolute; left: 420px; top: 400px; z-index: 3;
    font-family: 'Playfair Display', serif; font-weight: 900;
    font-size: 88px; line-height: 1; color: var(--title-red);
    text-shadow: 2px 2px 0 var(--title-shadow);
  }
  .ribbon {
    position: absolute; left: 90px; top: 530px; z-index: 4;
    width: 380px; height: 56px;
  }
  .ribbon svg { display: block; }
  .ribbon__text {
    position: absolute; left: 0; right: 0; top: 4px; height: 40px;
    display: flex; align-items: center; justify-content: center;
    font-family: 'Pinyon Script', cursive; font-size: 28px; color: var(--ink);
  }
  .details {
    position: absolute; left: 200px; right: 200px; top: 606px;
    display: flex; justify-content: space-between;
    font-family: 'Playfair Display', serif; font-weight: 700;
    font-size: 20px; color: var(--ink);
  }
</style>
</head>
<body>
<div class="canvas">
  <section class="label">
    <div class="label__frame"></div>

    <div class="maker"><span class="maker__dot"></span>Hartwell Distillers</div>

    <h1 class="product-name">Lantern<br>Down Lane</h1>

    <div class="scene" role="img" aria-label="Illustration of a country road stretching to the horizon"></div>
    <div class="traveller" role="img" aria-label="Illustration of a gentleman in a top hat walking away with a suitcase"></div>

    <div class="spirit">GIN</div>

    <div class="ribbon">
      <svg width="380" height="56" viewBox="0 0 380 56">
        <polygon points="0,12 30,12 30,50 0,50 14,31" fill="var(--ribbon-dark)"/>
        <polygon points="380,12 350,12 350,50 380,50 366,31" fill="var(--ribbon-dark)"/>
        <rect x="24" y="4" width="332" height="40" fill="var(--ribbon)" stroke="var(--ribbon-dark)" stroke-width="2"/>
      </svg>
      <span class="ribbon__text">Small Batch Craft Gin</span>
    </div>

    <div class="details"><span>50 cl</span><span>40% vol</span></div>
  </section>
</div>
</body>
</html>
```